Stationary Set and Logo Update **PAYMENT GUARANTEED**

Stationery Design and Logo Update

About Us

Trindex Supply is a wholesale distributor of OEM [original brand] and compatible [generic brand] parts and supplies for use in copiers, faxes, printers, and multi-function machines. In plain English…we sell all the parts and supplies [such as toner] that make up any office equipment which outputs an image on paper.

Trindex was the 1st distributor to develop and sell a generic brand copier part in the United States. We have been in business since 1972 [nearly 40 years]. Our tagline is "The Steady Choice," as in our company was the first alternative product that copier dealers had to buying original brand copier parts. Trindex is known for offering reliable and cost-effective OEM and compatible products.

Project

We require a fresh, modern and corporate identity. Please submit a stationary package inclusive of a double-sided business card (2" x 3.5"), letterhead (8.5'x11"), and standard #10 envelope (4-1/8” x 9-1/2). You may use our current logo or preferably your take on an updated one. If an attempt is made in updating the logo #004D8E or a similar hue should be used as the primary color.

The design should be clean, simple, modern and professional and make an immediate impact.

Target Market(s)

Copier and printer dealers who lease and service imaging equipment in the United States and Latin America.

Industry/Entity Type

Business

Requirements
Must have
• Simple, clean, modern and professional. Please use #004D8E or a similar hue as the primary color. Letterhead must accommate (2) addresses. We have 2 locations.
Nice to have
• A simple, modern update to our current logo. https://assets.mailvorbo.example/fs030/5520384417702/img/418.jpg
Should not have
• More than (2) colors on logo.

```html
<!DOCTYPE html>
<html lang="en">
<head>
<meta charset="utf-8">
<title>Trindex Supply – Stationery Set</title>
<link href="https://fonts.googleapis.com/css2?family=Roboto:wght@400;700;900&display=swap" rel="stylesheet">
<style>
  :root {
    --navy: #0b1a66;
    --blue: #004d8e;
    --royal: #1d4fc2;
    --sky: #5fa8ee;
    --ink: #1d1d1f;
    --charcoal: #222222;
    --grey: #8a8a8a;
    --paper: #ffffff;
    --line: #9a9a9a;
  }
  * { margin: 0; padding: 0; box-sizing: border-box; }
  html, body { width: 1200px; height: 900px; overflow: hidden; background: var(--paper); }
  body { position: relative; font-family: "Roboto", Arial, sans-serif; color: var(--ink); }

  .piece { position: absolute; overflow: hidden; }
  .piece > svg.bg { position: absolute; inset: 0; width: 100%; height: 100%; }

  .brand { position: absolute; display: flex; align-items: center; gap: 5px; font-weight: 900; color: var(--paper); letter-spacing: -0.3px; line-height: 1; white-space: nowrap; }
  .brand .dot { border-radius: 50%; background: var(--sky); flex: none; }
  .brand-sm { font-size: 17px; }
  .brand-sm .dot { width: 11px; height: 11px; }
  .brand-lg { font-size: 64px; color: var(--sky); letter-spacing: -1.5px; gap: 8px; }
  .brand-lg .dot { width: 34px; height: 34px; }

  /* envelope front */
  .envelope-front { left: 56px; top: 66px; width: 436px; height: 188px; }
  .envelope-front .brand-sm { left: 24px; top: 16px; }
  .envelope-front .brand-lg { left: 172px; top: 100px; }
  .address-window { position: absolute; left: 20px; top: 108px; width: 144px; height: 60px; background: #e9ecf1; border-radius: 6px; border: 1px solid #c8ccd4; }

  /* envelope back */
  .envelope-back { left: 56px; top: 262px; width: 436px; height: 196px; }
  .return-block { position: absolute; right: 14px; top: 54px; text-align: right; color: var(--paper); font-size: 6.5px; line-height: 1.22; }
  .return-block b { font-weight: 700; }
  .return-block .gap { height: 6px; }

  /* business cards */
  .card-front { left: 56px; top: 490px; width: 310px; height: 174px; background: var(--charcoal); border-radius: 7px; }
  .card-front .brand-sm { left: 22px; top: 20px; }
  .card-person { position: absolute; left: 22px; top: 88px; color: var(--paper); }
  .card-person .name { font-size: 13px; font-weight: 700; letter-spacing: 0.2px; }
  .card-person .title { font-size: 9px; color: #bdbdbd; margin-top: 4px; }
  .card-details { position: absolute; left: 168px; top: 20px; color: #d8d8d8; font-size: 7px; line-height: 1.35; }
  .card-details b { color: var(--paper); font-weight: 700; }
  .card-details .head { font-size: 8.5px; color: var(--paper); font-weight: 700; margin-bottom: 6px; }
  .card-details .gap { height: 6px; }

  .card-back { left: 56px; top: 678px; width: 310px; height: 174px; border-radius: 7px; }
  .card-back .brand-lg { left: 8px; top: 44px; font-size: 62px; gap: 8px; }
  .card-back .brand-lg .dot { width: 34px; height: 34px; }
  .card-back .brand-sm { right: 16px; bottom: 16px; font-size: 15px; }

  /* letterhead */
  .letterhead { left: 542px; top: 76px; width: 590px; height: 766px; background: var(--paper); border: 1px solid var(--line); }
  .letterhead .brand-sm { left: 40px; top: 40px; color: var(--blue); font-size: 18px; }
  .letterhead .brand-sm .dot { background: var(--blue); }
  .letterhead-contacts { position: absolute; top: 16px; left: 330px; display: flex; gap: 8px; font-size: 7.5px; line-height: 1.3; color: #777; }
  .letterhead-contacts .col-main { text-align: right; }
  .letterhead-contacts b { color: #555; font-weight: 700; }
</style>
</head>
<body>

<section class="piece envelope-front" aria-label="Envelope front">
  <svg class="bg" viewBox="0 0 436 188" preserveAspectRatio="none" aria-hidden="true">
    <defs>
      <linearGradient id="envFront" x1="0" y1="0" x2="1" y2="1">
        <stop offset="0" stop-color="#1a3aa8"/>
        <stop offset="0.55" stop-color="#0d1f80"/>
        <stop offset="1" stop-color="#0a1560"/>
      </linearGradient>
    </defs>
    <rect width="436" height="188" fill="url(#envFront)"/>
    <path d="M0 70 C120 40 260 40 436 90 L436 188 L0 188 Z" fill="#1c3fb0" opacity="0.45"/>
    <path d="M0 120 C150 90 300 100 436 150 L436 188 L0 188 Z" fill="#0a175c" opacity="0.6"/>
  </svg>
  <div class="brand brand-sm"><span class="dot"></span>Trindex</div>
  <div class="address-window"></div>
  <div class="brand brand-lg"><span class="dot"></span>Trindex</div>
</section>

<section class="piece envelope-back" aria-label="Envelope back">
  <svg class="bg" viewBox="0 0 436 196" preserveAspectRatio="none" aria-hidden="true">
    <defs>
      <linearGradient id="envBack" x1="0" y1="0" x2="1" y2="1">
        <stop offset="0" stop-color="#1f4fc4"/>
        <stop offset="1" stop-color="#0a1560"/>
      </linearGradient>
    </defs>
    <rect width="436" height="196" fill="url(#envBack)"/>
    <path d="M0 20 C160 10 320 30 436 80 L436 196 L0 196 Z" fill="#0e2286" opacity="0.55"/>
    <path d="M0 0 L30 0 C44 40 44 156 30 196 L0 196 Z" fill="#2a78d8"/>
    <path d="M30 0 C44 40 44 156 30 196" fill="none" stroke="#9cc8f5" stroke-width="1"/>
  </svg>
  <div class="return-block">
    <b>TRINDEX SUPPLY</b><br>
    <b>Corporate Office</b><br>
    2280 Harbor Park Drive<br>
    Fairhaven, FL 33410<br>
    Toll Free: 800-555-0142<br>
    Local: 954-555-0176<br>
    Fax: 954-555-0190
    <div class="gap"></div>
    <b>Trindex West</b><br>
    West Coast Fulfillment Center<br>
    North Ridge Business Park #2<br>
    915 Canyon Loop<br>
    Sparks Valley, NV 89502<br>
    Toll Free: 800-555-0118<br>
    Fax: 775-555-0163
  </div>
</section>

<section class="piece card-front" aria-label="Business card front">
  <div class="brand brand-sm"><span class="dot"></span>Trindex</div>
  <div class="card-person">
    <div class="name">Dara Welling</div>
    <div class="title">Marketing Coordinator</div>
  </div>
  <div class="card-details">
    <div class="head">Trindex Supply</div>
    <b>Corporate Office</b><br>
    2280 Harbor Park Drive<br>
    Fairhaven, FL 33410<br>
    Toll Free: 800-555-0142<br>
    Direct: 954-555-0176<br>
    Email: dwelling@trindex.example
    <div class="gap"></div>
    <b>Trindex West</b><br>
    West Coast Fulfillment Center<br>
    North Ridge Business Park #2<br>
    915 Canyon Loop<br>
    Sparks Valley, NV 89502
  </div>
</section>

<section class="piece card-back" aria-label="Business card back">
  <svg class="bg" viewBox="0 0 310 174" preserveAspectRatio="none" aria-hidden="true">
    <defs>
      <linearGradient id="cardBack" x1="0" y1="0" x2="1" y2="1">
        <stop offset="0" stop-color="#1f4fc4"/>
        <stop offset="1" stop-color="#0a1560"/>
      </linearGradient>
    </defs>
    <rect width="310" height="174" rx="7" fill="url(#cardBack)"/>
    <path d="M0 40 C100 20 220 30 310 70 L310 174 L0 174 Z" fill="#0e2286" opacity="0.5"/>
    <path d="M0 120 C110 100 220 110 310 150 L310 174 L0 174 Z" fill="#0a175c" opacity="0.55"/>
  </svg>
  <div class="brand brand-lg"><span class="dot"></span>Trindex</div>
  <div class="brand brand-sm"><span class="dot"></span>Trindex</div>
</section>

<section class="piece letterhead" aria-label="Letterhead">
  <svg class="bg" viewBox="0 0 590 766" preserveAspectRatio="none" aria-hidden="true">
    <defs>
      <linearGradient id="swoosh" x1="0" y1="0" x2="1" y2="0">
        <stop offset="0" stop-color="#0a1560"/>
        <stop offset="1" stop-color="#1f4fc4"/>
      </linearGradient>
    </defs>
    <path d="M0 0 L150 0 C80 6 20 36 0 100 Z" fill="url(#swoosh)"/>
    <path d="M0 0 L110 0 C60 8 18 30 0 64 Z" fill="#0a175c" opacity="0.5"/>
  </svg>
  <div class="brand brand-sm"><span class="dot"></span>Trindex</div>
  <div class="letterhead-contacts">
    <div class="col-main">
      <b>TRINDEX SUPPLY</b><br>
      <b>Corporate Office</b><br>
      2280 Harbor Park Drive<br>
      Fairhaven, FL 33410<br>
      Toll Free: 800-555-0142<br>
      Local: 954-555-0176<br>
      Fax: 954-555-0190
    </div>
    <div class="col-west">
      <b>Trindex West</b><br>
      West Coast Fulfillment Center<br>
      North Ridge Business Park #2<br>
      915 Canyon Loop<br>
      Sparks Valley, NV 89502<br>
      Toll Free: 800-555-0118<br>
      Fax: 775-555-0163
    </div>
  </div>
</section>

</body>
</html>
```